We need a wesbite for a new company based in London called: 'Ashbourne Maids'. We supply the following services in private household: nanny, housekeeper, maternity nurse, driver, carer, companion and cleaner.
We would like to see designs that should communicate good ethics and high standard, quality services and professionalism.

I want a website something like: www.brightnestcarers.co.uk and http://www.tidyhearthstaff.co.uk/ I want the landing page should have at least 3 seconds intervals of changing photos of Asian (only) particularly Filipino (from the Philippines) Nanny with Children, Asian Housekeeper with apron cleaning, a photo of elderly in a wheelchair with the carer and a picture of a happy family with asian nanny in the background cleaning.

```html
<!DOCTYPE html>
<html lang="en">
<head>
<meta charset="utf-8">
<title>Ashbourne Maids</title>
<link href="https://fonts.googleapis.com/css2?family=Open+Sans:ital,wght@0,400;0,600;0,700;1,400&family=Roboto+Condensed:wght@400;700&display=swap" rel="stylesheet">
<style>
:root{
  --blue:#1b7fd1;
  --blue-dark:#1559a8;
  --blue-deep:#0f4c93;
  --sky:#1aa3e0;
  --nav:#2492dc;
  --ink:#333333;
  --muted:#666666;
  --light:#f4f5f6;
  --footer:#15171a;
  --white:#ffffff;
  --gold:#f0b429;
}
*{box-sizing:border-box;margin:0;padding:0}
html,body{width:1200px;height:2503px;overflow:hidden}
body{font-family:"Open Sans",sans-serif;color:var(--ink);background:var(--white);position:relative}
.head,.title,.card-label,.nav a,.btn{font-family:"Roboto Condensed",sans-serif}

/* header */
.site-header{position:absolute;top:0;left:0;width:1200px;height:120px;background:var(--white)}
.brand{position:absolute;left:98px;top:30px;display:flex;align-items:center;gap:12px}
.brand-dot{width:60px;height:60px;border-radius:50%;background:var(--blue)}
.brand-name{font-family:"Roboto Condensed",sans-serif;font-size:40px;font-weight:400;color:var(--blue)}
.contact-top{position:absolute;left:714px;top:33px;display:flex;gap:14px;align-items:center}
.contact-top p{font-size:14px;color:var(--muted);line-height:22px}
.socials{position:absolute;left:994px;top:45px;display:flex;gap:6px}
.socials span{width:22px;height:22px;border-radius:50%;background:#8aa0b8}
.socials span:nth-child(1){background:#3b5a9a}
.socials span:nth-child(2){background:#2aa6de}
.socials span:nth-child(3){background:#c93a2c}
.socials span:nth-child(4){background:#b9bec4}

/* nav */
.nav{position:absolute;top:120px;left:0;width:1200px;height:47px;background:var(--nav);display:flex;padding-left:98px}
.nav a{color:var(--white);text-decoration:none;font-size:13px;line-height:47px;padding:0 24px;letter-spacing:.3px}
.nav a.active{background:#46a9ea}

/* hero */
.hero{position:absolute;top:167px;left:0;width:1200px;height:501px;background:linear-gradient(100deg,#4d6b3a 0%,#7f9a5a 30%,#a8a68c 55%,#4c5a7a 80%,#6d7a6a 100%)}
.hero-title{position:absolute;left:97px;top:183px;font-family:"Roboto Condensed",sans-serif;font-weight:700;font-size:50px;line-height:50px;color:var(--white)}
.btn-appoint{position:absolute;left:98px;top:293px;width:211px;height:40px;background:var(--blue);color:var(--white);font-size:15px;font-weight:700;text-align:center;line-height:40px}
.hero-arrow{position:absolute;top:210px}

/* welcome */
.welcome{position:absolute;top:668px;left:0;width:1200px;height:267px;background:var(--light)}
.welcome h2{position:absolute;top:50px;width:100%;text-align:center;font-family:"Roboto Condensed",sans-serif;font-weight:400;font-size:30px;color:#333}
.welcome p{position:absolute;top:98px;left:138px;width:924px;text-align:center;font-size:11.5px;line-height:20px;color:#555}
.cards{position:absolute;top:871px;left:98px;display:flex;gap:15px}
.card{width:324px;height:227px;border:2px solid var(--blue);border-radius:10px;overflow:hidden;position:relative;background:var(--blue)}
.card-photo{position:absolute;top:0;left:0;width:100%;height:170px}
.card svg.wave{position:absolute;top:150px;left:0}
.card-label{position:absolute;left:16px;bottom:14px;color:var(--white);font-size:17px}
.card-more{position:absolute;right:12px;bottom:14px;color:var(--white);font-size:11px;font-weight:700}

/* services */
.services{position:absolute;top:1165px;left:0;width:1200px;height:459px;background:linear-gradient(90deg,#1557a8,#1d63b5 50%,#1453a0)}
.services h2{position:absolute;top:55px;width:100%;text-align:center;font-family:"Roboto Condensed",sans-serif;font-weight:700;font-size:30px;color:var(--white)}
.service{position:absolute;top:140px;width:350px;text-align:center;color:var(--white)}
.service .icon{width:110px;height:110px;margin:0 auto;border-radius:50%;background:var(--white);display:flex;align-items:center;justify-content:center;box-shadow:0 0 0 4px rgba(255,255,255,.35)}
.service h3{font-family:"Roboto Condensed",sans-serif;font-weight:400;font-size:19px;margin-top:28px}
.service p{font-size:11px;line-height:21px;margin-top:10px;padding:0 10px}
.service .more{font-size:11px;font-weight:700;margin-top:12px}

/* testimonials & blog */
.section-title{position:absolute;top:1683px;font-family:"Roboto Condensed",sans-serif;font-weight:400;font-size:31px;color:#333}
.pager{position:absolute;top:1695px;font-size:13px;color:#444;letter-spacing:8px}
.testimonial{position:absolute;top:1739px;left:98px;width:483px;height:247px;border:1px solid #ddd;box-shadow:0 1px 4px rgba(0,0,0,.12);background:var(--white)}
.testimonial blockquote{position:absolute;left:22px;top:28px;width:290px;font-style:italic;font-size:11px;line-height:20px;color:#555}
.testimonial .author{position:absolute;left:22px;top:138px;font-style:italic;font-size:11px;line-height:20px;color:#444}
.stars{position:absolute;left:22px;top:186px;font-size:11px;color:var(--gold);letter-spacing:1px}
.stars span{color:#ccc}
.testimonial-photo{position:absolute;right:0;top:0;width:186px;height:245px;border-radius:160px 0 0 0 / 245px 0 0 0}
.post{position:absolute;top:1739px;width:227px}
.post-photo{width:227px;height:177px}
.post time{display:block;margin-top:14px;font-size:12px;color:var(--blue);font-weight:600}
.post p{margin-top:6px;font-family:"Roboto Condensed",sans-serif;font-size:15px;line-height:19px;color:#444}

/* help band */
.help{position:absolute;top:2056px;left:0;width:1200px;height:101px;background:var(--sky)}
.help h2{position:absolute;left:98px;top:22px;font-family:"Roboto Condensed",sans-serif;font-weight:400;font-size:26px;color:var(--white);letter-spacing:.5px}
.help p{position:absolute;left:98px;top:60px;font-size:11px;color:var(--white)}
.btn-enquiry{position:absolute;left:945px;top:27px;width:156px;height:47px;border:2px solid var(--white);border-radius:3px;background:var(--blue-deep);color:var(--white);font-size:14px;text-align:center;line-height:43px}

/* footer */
.footer{position:absolute;top:2157px;left:0;width:1200px;height:293px;background:var(--footer);color:var(--white)}
.footer h4{font-family:"Roboto Condensed",sans-serif;font-weight:400;font-size:20px;position:absolute;top:45px}
.footer .about{position:absolute;left:98px;top:90px;width:210px;font-size:11px;line-height:20px;color:#ddd}
.field{position:absolute;border:1px solid #bbb;font-size:10px;color:#ddd;padding:10px 12px}
.submit{position:absolute;left:359px;top:218px;width:108px;height:34px;border:1px solid #ccc;border-radius:3px;font-family:"Roboto Condensed",sans-serif;font-weight:700;font-size:15px;text-align:center;line-height:32px}
.contact{position:absolute;left:718px;top:90px;font-size:12px;line-height:20px;color:#ddd}
.contact-line{display:flex;gap:14px;align-items:center;margin-top:12px}
.links{position:absolute;left:990px;top:88px;list-style:none;font-size:12px;line-height:23px;color:#ddd}
.links li::before{content:"";display:inline-block;border-left:5px solid #ddd;border-top:4px solid transparent;border-bottom:4px solid transparent;margin-right:12px}

.bottom-bar{position:absolute;top:2450px;left:0;width:1200px;height:53px;background:var(--sky);color:var(--white);font-size:12px;text-align:center;line-height:53px}
</style>
</head>
<body>

<header class="site-header">
  <div class="brand"><span class="brand-dot"></span><span class="brand-name">Ashbourne Maids</span></div>
  <div class="contact-top">
    <svg width="24" height="30" viewBox="0 0 24 30"><path d="M6 2 C2 4 1 10 5 17 C9 24 15 28 19 27 L22 23 L17 19 L14 21 C11 19 9 15 8 11 L11 9 L9 3 Z" fill="#c7c9cc"/></svg>
    <div><p>info@ashbournemaids.co.uk</p><p>Phone : (020) - 555 - 0148</p></div>
  </div>
  <div class="socials"><span></span><span></span><span></span><span></span></div>
</header>

<nav class="nav">
  <a class="active">HOME</a><a>ABOUT US</a><a>OUR SERVICES</a><a>TYPES OF HELP AVAILABLE</a><a>MEET THE TEAM</a><a>BLOG</a><a>CONTACT US</a>
</nav>

<section class="hero" role="img" aria-label="Smiling nanny holding a young child outdoors in a garden">
  <svg class="hero-arrow" style="left:30px" width="30" height="60" viewBox="0 0 30 60"><path d="M26 2 L4 30 L26 58" stroke="#fff" stroke-width="2" fill="none"/></svg>
  <svg class="hero-arrow" style="left:1140px" width="30" height="60" viewBox="0 0 30 60"><path d="M4 2 L26 30 L4 58" stroke="#fff" stroke-width="2" fill="none"/></svg>
  <h1 class="hero-title">ASHBOURNE<br>MAIDS</h1>
  <div class="btn-appoint">MAKE AN APPOINTMENT</div>
</section>

<section class="welcome">
  <h2>WELCOME TO ASHBOURNE MAIDS</h2>
  <p>Sed ut perspiciatis unde omnis iste natus error sit voluptatem accusantium doloremque laudantium, totam rem aperiam, eaque ipsa quae ab illo inventore veritatis et quasi architecto beatae vitae dicta sunt explicabo. Nemo enim ipsam voluptatem quia voluptas sit aspernatur aut odit aut fugit, sed quia consequuntur magni dolores eos qui ratione voluptatem sequi nesciunt. Neque porro quisquam est, qui dolorem ipsum quia dolor sit amet, consectetur, adipisci velit, sed quia non numquam</p>
</section>

<div class="cards">
  <div class="card">
    <div class="card-photo" role="img" aria-label="Housekeeper in uniform standing in a tidy bedroom" style="background:linear-gradient(120deg,#e9e2d6,#c9b69a 60%,#8b7660)"></div>
    <svg class="wave" width="324" height="40" viewBox="0 0 324 40"><path d="M0 22 C90 0 200 40 324 12 L324 40 L0 40 Z" fill="#1b6fc8"/></svg>
    <span class="card-label">HOUSEKEEPER</span><span class="card-more">READ MORE ➜</span>
  </div>
  <div class="card">
    <div class="card-photo" role="img" aria-label="Maternity nurse with new parents and their baby" style="background:linear-gradient(120deg,#cfe3ea,#9ec8d6 45%,#d8cfc2)"></div>
    <svg class="wave" width="324" height="40" viewBox="0 0 324 40"><path d="M0 22 C90 0 200 40 324 12 L324 40 L0 40 Z" fill="#1b6fc8"/></svg>
    <span class="card-label">MATERNITY NURSE</span><span class="card-more">READ MORE ➜</span>
  </div>
  <div class="card">
    <div class="card-photo" role="img" aria-label="Nanny playing with two children" style="background:linear-gradient(120deg,#b9865a,#d9a36a 50%,#e3c25a)"></div>
    <svg class="wave" width="324" height="40" viewBox="0 0 324 40"><path d="M0 22 C90 0 200 40 324 12 L324 40 L0 40 Z" fill="#1b6fc8"/></svg>
    <span class="card-label">NANNY</span><span class="card-more">READ MORE ➜</span>
  </div>
</div>

<section class="services">
  <h2>OUR SERVICES</h2>
  <div class="service" style="left:79px">
    <div class="icon"><svg width="50" height="50" viewBox="0 0 50 50"><path d="M32 4 L20 34" stroke="#1559a8" stroke-width="4" stroke-linecap="round"/><path d="M12 32 L28 38 L24 48 L6 42 Z" fill="#1559a8"/></svg></div>
    <h3>COMPANION AND CLEANER</h3>
    <p>Sed ut perspiciatis unde omnis iste natus error sit voluptatem accusantium doloremque laudantium, totam rem aperiam, eaque ipsa quae ab illo inventore</p>
    <div class="more">READ MORE ➜</div>
  </div>
  <div class="service" style="left:429px">
    <div class="icon"><svg width="50" height="50" viewBox="0 0 50 50"><circle cx="25" cy="25" r="19" stroke="#1559a8" stroke-width="5" fill="none"/><circle cx="25" cy="25" r="5" fill="#1559a8"/><path d="M7 22 L43 22 M25 30 L25 44" stroke="#1559a8" stroke-width="5"/></svg></div>
    <h3>DRIVER SERVICES</h3>
    <p>Sed ut perspiciatis unde omnis iste natus error sit voluptatem accusantium doloremque laudantium, totam rem aperiam, eaque ipsa quae ab illo inventore</p>
    <div class="more">READ MORE ➜</div>
  </div>
  <div class="service" style="left:780px">
    <div class="icon"><svg width="50" height="50" viewBox="0 0 50 50"><path d="M25 44 C8 32 4 24 4 16 C4 9 10 5 15 5 C20 5 23 8 25 12 C27 8 30 5 35 5 C40 5 46 9 46 16 C46 24 42 32 25 44 Z" fill="#1559a8"/></svg></div>
    <h3>CARER SERVICES</h3>
    <p>Sed ut perspiciatis unde omnis iste natus error sit voluptatem accusantium doloremque laudantium, totam rem aperiam, eaque ipsa quae ab illo inventore</p>
    <div class="more">READ MORE ➜</div>
  </div>
</section>

<h2 class="section-title" style="left:98px">TESTIMONIALS</h2>
<div class="pager" style="left:546px">←→</div>
<div class="testimonial">
  <blockquote>“ Sed ut perspiciatis unde omnis iste natus error sit voluptatem accusantium doloremque. Nam libero tempore, cum soluta nobis est eligendi optio cumque nihil impedit quo minus id quod maxime placeat facere possimus, omnis</blockquote>
  <div class="author">- MARIA DELANO<br>FOUNDER OF XYZ COMPANY</div>
  <div class="stars">★★★<span>★★</span></div>
  <div class="testimonial-photo" role="img" aria-label="Smiling cleaner holding cleaning supplies" style="background:linear-gradient(160deg,#e8e4dc,#c9bfae 60%,#9a8e7a)"></div>
</div>

<h2 class="section-title" style="left:623px">LATEST BLOG</h2>
<div class="pager" style="left:1066px">←→</div>
<article class="post" style="left:623px">
  <div class="post-photo" role="img" aria-label="Girl playing with toy blocks with a carer" style="background:linear-gradient(140deg,#8c6a4e,#c9a07a 50%,#d35b45)"></div>
  <time>Aug 20, 2016</time>
  <p>Sed ut perspiciatis unde omnis iste natus error sit voluptatem</p>
</article>
<article class="post" style="left:873px">
  <div class="post-photo" role="img" aria-label="Nurse in scrubs smiling with a child at a table" style="background:linear-gradient(140deg,#d6b56a,#caa468 45%,#3aa79a)"></div>
  <time>Aug 20, 2016</time>
  <p>Sed ut perspiciatis unde omnis iste natus error sit voluptatem</p>
</article>

<section class="help">
  <h2>TYPES OF HELP AVAILABLE</h2>
  <p>Lorem ipsum dolor sit amet, consectetur adipiscing elit, sed do eiusmod tempor incididunt ut labore et dolore</p>
  <div class="btn-enquiry">QUICK ENQUIRY ➜</div>
</section>

<footer class="footer">
  <h4 style="left:98px">ABOUT US</h4>
  <p class="about">Sed ut perspiciatis unde omnis iste natus error sit voluptatem usantium doloremque laudantium, totam rem aperiam, eaque ipsa quae ab illo inventore veritatis et quasi rchitecto beatae vitae dicta sunt explicabo. Nemo enim ipsam</p>

  <h4 style="left:359px;top:40px">QUICK ENQUIRY</h4>
  <div class="field" style="left:359px;top:90px;width:147px;height:38px">Name</div>
  <div class="field" style="left:514px;top:90px;width:145px;height:38px">Phone</div>
  <div class="field" style="left:359px;top:135px;width:300px;height:70px">Message</div>
  <div class="submit">SUBMIT</div>

  <h4 style="left:718px">CONTACT US</h4>
  <div class="contact">
    <p>Ashbourne Maids<br>Elmfield Road, Marlow Quarter,<br>London, United Kingdom</p>
    <div class="contact-line"><svg width="16" height="18" viewBox="0 0 24 30"><path d="M6 2 C2 4 1 10 5 17 C9 24 15 28 19 27 L22 23 L17 19 L14 21 C11 19 9 15 8 11 L11 9 L9 3 Z" fill="none" stroke="#ddd" stroke-width="2"/></svg>Phone: +44 20 7946 0321</div>
    <div class="contact-line"><svg width="18" height="13" viewBox="0 0 18 13"><rect x="1" y="1" width="16" height="11" fill="none" stroke="#ddd" stroke-width="1.5"/><path d="M1 1 L9 8 L17 1" fill="none" stroke="#ddd" stroke-width="1.5"/></svg>Email: hello@ashbournemaids.co.uk</div>
  </div>

  <h4 style="left:990px;top:40px">QUICK LINKS</h4>
  <ul class="links"><li>Home</li><li>About</li><li>Applicants</li><li>Services</li><li>Testimonial</li><li>News</li><li>Contact</li></ul>
</footer>

<div class="bottom-bar">Copyright 2016 | All Rights Reserved – Ashbourne Maids</div>

</body>
</html>
```